Varnell Skyworks Limited

Started a consulting business 12 months ago and have since moved location and have grown and seek to identify my self to the industry.
Specializing in quality solutions, business documentation and maintenance solution's

Industry/Entity Type

Business

```html
<!DOCTYPE html>
<html lang="en">
<head>
<meta charset="utf-8">
<title>Varnell Skyworks Limited — Business Card</title>
<link href="https://fonts.googleapis.com/css2?family=Quicksand:wght@400;500&display=swap" rel="stylesheet">
<style>
  :root {
    --backdrop: #262626;
    --frame-bronze: #5b3f18;
    --frame-edge: #3e2a0e;
    --face-gold-light: #c4ae8e;
    --face-gold: #b49d7c;
    --face-gold-dark: #a38c6b;
    --ink: #2a1f12;
    --dot: #a58c68;
    --dot-shadow: #7d6545;
  }
  html, body {
    margin: 0;
    padding: 0;
    width: 1200px;
    height: 1000px;
    overflow: hidden;
    background: var(--backdrop);
  }
  .card {
    position: absolute;
    left: 180px;
    top: 244px;
    width: 840px;
    height: 512px;
    box-sizing: border-box;
    padding: 16px;
    background: var(--frame-bronze);
    border: 2px solid var(--frame-edge);
    border-radius: 4px;
    box-shadow: 0 18px 40px rgba(0,0,0,0.55);
  }
  .card-face {
    position: relative;
    width: 100%;
    height: 100%;
    border-radius: 2px;
    box-shadow: inset 0 0 0 1px rgba(60,40,15,0.6);
    background:
      repeating-linear-gradient(180deg,
        rgba(255,255,255,0.05) 0px, rgba(255,255,255,0.05) 1px,
        rgba(0,0,0,0.04) 2px, rgba(0,0,0,0) 3px),
      linear-gradient(160deg, var(--face-gold-light) 0%, var(--face-gold) 50%, var(--face-gold-dark) 100%);
  }
  .contact {
    position: absolute;
    top: 68px;
    left: 0;
    right: 0;
    text-align: center;
    font-family: "Quicksand", sans-serif;
    font-weight: 500;
    font-size: 25px;
    line-height: 30px;
    color: var(--ink);
  }
  .contact p { margin: 0; }
  .contact .group + .group { margin-top: 30px; }
  .dot-row {
    position: absolute;
    left: 50%;
    bottom: 60px;
    transform: translateX(-50%);
    display: flex;
    gap: 24px;
  }
  .dot-row span {
    width: 14px;
    height: 14px;
    border-radius: 50%;
    background: var(--dot);
    box-shadow: inset 1px 2px 2px var(--dot-shadow);
  }
</style>
</head>
<body>
  <div class="card">
    <div class="card-face">
      <div class="contact">
        <div class="group">
          <p class="company-name">Varnell Skyworks Limited</p>
          <p class="person-name">Darren T Holloway</p>
        </div>
        <div class="group address">
          <p>Unit B014, 52 Kerrigan Road</p>
          <p>Mount Wellesley 2016</p>
          <p>Auckland NZ</p>
        </div>
        <div class="group">
          <p class="phone">Mobile +64 21 555 0147</p>
          <p class="email">Email : info@varnellsky.co.nz</p>
        </div>
      </div>
      <div class="dot-row" aria-hidden="true">
        <span></span><span></span><span></span><span></span><span></span>
        <span></span><span></span><span></span><span></span><span></span>
      </div>
    </div>
  </div>
</body>
</html>
```